Start up in business consultancy needs a business card

We need the business card's layout (we have already the logo). Our business is concerned on consultancy services delivered to companies on the matter of sustainability. Business card should be enough essentials and professional style.

Side A with the following info:
logo + a space for the claim (still to identify) + website of the company

Side B with the following info:
Name of business card holder + title of the business card holder + address of the company + space for mobile number, phone number, fax number + e-mail of business card holder + graphic details around.

Target Market(s)

Business of any sector

Industry/Entity Type

Business Service

Contact Information for Business Card

Name of the company:
Pianoverde srl
Società Benefit

Address of the company:
Via Lucerna, 7
21047 - Saronno (VA)

Website:
www.pianoverde.it

Name of the BC' holder:
Luca Ferentino

Title:
Co-fondatore

Email:
luca@pianoverde.it

Mobile:
+39 348 915 2074
Phone:
+39 348 915 2074
Fax:
+39 348 915 2074

Font styles to use
Other font styles liked:
• new gothic

```html
<!DOCTYPE html>
<html lang="it">
<head>
<meta charset="utf-8">
<title>Pianoverde – biglietto da visita</title>
<link rel="stylesheet" href="https://fonts.googleapis.com/css2?family=Montserrat:wght@300;400;600;700&display=swap">
<style>
  :root {
    --stage: #8c8c8c;
    --brand-blue: #0a67b0;
    --brand-blue-deep: #085a9c;
    --paper: #ffffff;
    --ink-light: #e6f0f9;
  }
  * { margin: 0; padding: 0; box-sizing: border-box; }
  html, body { width: 1200px; height: 900px; overflow: hidden; }
  body {
    background: var(--stage);
    font-family: "Montserrat", sans-serif;
    display: flex; flex-direction: column; align-items: center; justify-content: center;
    gap: 40px;
  }
  .card {
    width: 660px; height: 377px; border-radius: 30px; overflow: hidden; position: relative;
    box-shadow: 0 10px 24px rgba(0,0,0,.25);
  }
  .card--front {
    background: linear-gradient(135deg, var(--brand-blue) 0%, var(--brand-blue-deep) 100%);
    color: var(--paper);
    display: flex; flex-direction: column; align-items: center; justify-content: center;
  }
  .brand { display: flex; align-items: center; gap: 16px; }
  .brand__dot { width: 62px; height: 62px; border-radius: 50%; border: 4px solid currentColor; }
  .brand__name { font-weight: 600; font-size: 52px; letter-spacing: .5px; }
  .card--front .website {
    margin-top: 34px; font-weight: 300; font-size: 15px; letter-spacing: 2px;
  }
  .card--back { background: var(--paper); }
  .card--back .top {
    height: 168px; display: flex; align-items: center; justify-content: center;
    color: var(--brand-blue);
  }
  .card--back .brand__dot { width: 52px; height: 52px; border-width: 4px; }
  .card--back .brand__name { font-size: 42px; }
  .card--back .bottom {
    position: absolute; left: 0; right: 0; bottom: 0; height: 209px;
    background: linear-gradient(135deg, var(--brand-blue) 0%, var(--brand-blue-deep) 100%);
    color: var(--ink-light);
    display: flex; align-items: center; padding: 0 44px;
  }
  .holder { width: 270px; }
  .holder__name { font-weight: 700; font-size: 22px; text-transform: uppercase; color: var(--paper); letter-spacing: .5px; }
  .holder__title { font-weight: 400; font-size: 14px; text-transform: uppercase; margin-top: 6px; }
  .holder__address { font-weight: 300; font-size: 13px; text-transform: uppercase; margin-top: 16px; line-height: 1.5; }
  .divider { width: 1px; height: 130px; background: rgba(255,255,255,.55); margin: 0 34px; }
  .contacts { list-style: none; font-weight: 300; font-size: 15px; }
  .contacts li { display: flex; align-items: center; gap: 12px; margin: 7px 0; }
  .contacts svg { width: 20px; height: 20px; fill: none; stroke: var(--paper); stroke-width: 1.5; }
</style>
</head>
<body>
  <section class="card card--front">
    <div class="brand">
      <span class="brand__dot"></span>
      <span class="brand__name">pianoverde</span>
    </div>
    <p class="website">www.pianoverde.it</p>
  </section>

  <section class="card card--back">
    <div class="top">
      <div class="brand">
        <span class="brand__dot"></span>
        <span class="brand__name">pianoverde</span>
      </div>
    </div>
    <div class="bottom">
      <div class="holder">
        <p class="holder__name">Luca Ferentino</p>
        <p class="holder__title">Co-fondatore</p>
        <p class="holder__address">Via Lucerna, 7<br>21047 - Saronno (VA)</p>
      </div>
      <span class="divider"></span>
      <ul class="contacts">
        <li><svg viewBox="0 0 20 20" aria-hidden="true"><rect x="6" y="2" width="8" height="16" rx="1.5"/><line x1="9" y1="15.5" x2="11" y2="15.5"/></svg>+39 348 915 2074</li>
        <li><svg viewBox="0 0 20 20" aria-hidden="true"><path d="M5 3l3 3-2 2c1 2 3 4 6 6l2-2 3 3-2 2C9 17 3 11 3 5z"/></svg>+39 348 915 2074</li>
        <li><svg viewBox="0 0 20 20" aria-hidden="true"><rect x="3" y="8" width="14" height="9" rx="1"/><rect x="6" y="3" width="8" height="5"/><line x1="6" y1="12" x2="14" y2="12"/></svg>+39 348 915 2074</li>
        <li><svg viewBox="0 0 20 20" aria-hidden="true"><rect x="2" y="4" width="16" height="12"/><path d="M2 4l8 7 8-7M2 16l6-6M18 16l-6-6"/></svg>luca@pianoverde.it</li>
      </ul>
    </div>
  </section>
</body>
</html>
```